Business Card Design for Logistics Startup

Link to my logo source file -
https://www.fylvault.com/sh/qormx7pl2vkc8wd/KLmrT9_ZPq4BnWvHhYtaeCxo?dl=0

We want a statement in our business card!
I have go thru your portfolio, and invites 3 of you guys to design my business card as the previous designer cannot give me the feel.
Let me know if you want any information.
Thanks.
Updates

Target Market(s)

Transport and Logistics
: Shippers, Freight Forwarders and Carriers.

Industry/Entity Type

Business

Contact Information for Business Card

Our details;

Name: Marcus Loh
Designation: General Manager
Mobile: +65 91234508
Email: marcus.loh@corvinmarl.com
Address: 7 Lorong Pelita Rise
RHOMB Tower #09-17
Singapore 639217

Name: Victor Yeo
Designation: Director
Mobile: +65 93416672
Email: victor.yeo@corvinmarl.com
RHOMB Tower #09-17
Singapore 639217

Colors
f37122

Requirements
Must have
• Logo from my source file.
• Please included tagline: Transport and Logistics
• If you guy can think of a tagline - Using E and S, that will be perfect. Such as Excellence in Service..

```html
<!DOCTYPE html>
<html lang="en">
<head>
<meta charset="utf-8">
<title>Corvinmarl Business Card</title>
<link href="https://fonts.googleapis.com/css2?family=Nunito+Sans:wght@300;400&display=swap" rel="stylesheet">
<style>
  :root {
    --stage: #111111;
    --card: #000000;
    --gold-dark: #a69e52;
    --gold-mid: #c9c07c;
    --gold-light: #e4dba2;
    --gold-bright: #e8e46a;
    --gold-text: #c2b98a;
    --band: linear-gradient(90deg, #cfc78a 0%, #e2d9a0 18%, #a9a153 34%, #e4dba4 52%, #b3ab62 68%, #dfd69c 84%, #c4bc7c 100%);
  }
  * { margin: 0; padding: 0; box-sizing: border-box; }
  html, body { width: 1200px; height: 1000px; overflow: hidden; background: var(--stage); }
  body { position: relative; font-family: "Nunito Sans", sans-serif; color: var(--gold-text); }

  .card {
    position: absolute; left: 258px; width: 683px; height: 390px;
    background: var(--card); overflow: hidden;
    box-shadow: 0 10px 30px rgba(0,0,0,0.6);
  }
  .card--front { top: 96px; }
  .card--back { top: 518px; }

  .band { position: absolute; left: 0; right: 0; background: var(--band); }
  .band--top { top: 0; height: 28px; }
  .band--bottom { bottom: 0; height: 30px; }
  .rule { position: absolute; left: 0; right: 0; height: 4px; background: var(--band); }
  .card--front .rule--top { top: 31px; background: var(--gold-bright); }
  .card--front .rule--bottom { bottom: 32px; }
  .card--back .rule--top { top: 30px; }
  .card--back .rule--bottom { bottom: 33px; }

  .brand {
    position: absolute; text-align: center; transform: translate(-50%, -50%);
    white-space: nowrap;
  }
  .card--front .brand { left: 342px; top: 194px; }
  .card--back .brand { left: 174px; top: 195px; }
  .brand__name {
    display: flex; align-items: center; justify-content: center; gap: 12px;
    font-weight: 300; font-size: 36px; letter-spacing: 5px; color: var(--gold-mid);
  }
  .brand__dot { width: 12px; height: 12px; border-radius: 50%; background: var(--gold-mid); }
  .brand__tagline {
    margin-top: 12px; font-weight: 300; font-size: 14px; letter-spacing: 5px; color: var(--gold-mid);
  }

  .divider { position: absolute; left: 340px; top: 88px; width: 2px; height: 212px; background: var(--gold-mid); }

  .contact { position: absolute; left: 385px; top: 104px; line-height: 1.15; }
  .contact__name { font-weight: 400; font-size: 28px; letter-spacing: 0.5px; color: var(--gold-text); }
  .contact__role { font-size: 17px; margin-top: 2px; }
  .contact__lines { margin-top: 16px; font-size: 17px; list-style: none; }
  .contact__lines li { display: flex; align-items: center; gap: 9px; height: 20px; }
  .contact__lines svg { width: 14px; height: 14px; flex: none; }
  .contact__address { margin-top: 14px; font-size: 17px; font-style: normal; line-height: 1.12; }
</style>
</head>
<body>
  <section class="card card--front">
    <div class="band band--top"></div>
    <div class="rule rule--top"></div>
    <div class="brand">
      <div class="brand__name"><span class="brand__dot"></span>CORVINMARL</div>
      <div class="brand__tagline">TRANSPORT &amp; LOGISTICS</div>
    </div>
    <div class="rule rule--bottom"></div>
    <div class="band band--bottom"></div>
  </section>

  <section class="card card--back">
    <div class="band band--top"></div>
    <div class="rule rule--top"></div>
    <div class="brand">
      <div class="brand__name"><span class="brand__dot"></span>CORVINMARL</div>
      <div class="brand__tagline">TRANSPORT &amp; LOGISTICS</div>
    </div>
    <div class="divider"></div>
    <div class="contact">
      <div class="contact__name">MARCUS LOH</div>
      <div class="contact__role">General Manager</div>
      <ul class="contact__lines">
        <li>
          <svg viewBox="0 0 14 14" aria-hidden="true"><rect x="3.5" y="1" width="7" height="12" rx="1.2" fill="none" stroke="#c2b98a" stroke-width="1.4"/><line x1="6" y1="11" x2="8" y2="11" stroke="#c2b98a" stroke-width="1.2"/></svg>
          +65 91 23 4508
        </li>
        <li>
          <svg viewBox="0 0 14 14" aria-hidden="true"><rect x="0.5" y="2.5" width="13" height="9" fill="#c2b98a"/><path d="M0.5 2.5 L7 8 L13.5 2.5" fill="none" stroke="#000" stroke-width="1.2"/></svg>
          marcus.loh@corvinmarl.com
        </li>
      </ul>
      <address class="contact__address">
        7 Lorong Pelita Rise<br>
        RHOMB Tower #09-17<br>
        Singapore 639217
      </address>
    </div>
    <div class="rule rule--bottom"></div>
    <div class="band band--bottom"></div>
  </section>
</body>
</html>
```